Simple, High-Class Web Design Wanted - Motivational Speakers Site

1. Full Brief/Request & Specs outlined on following video -
http://clipvane-recorder.com/watch/tbWrkLmQyP

2. Use colours, images as you feel suits objective (we are happy to pay up to US$30 for any good images but must have licence/permission).

3. Layout probably similar to existing site - www.podiumvoicehub.com.au / http://podiumvoicehub.com.au/contact.php

4. Must Be Able to Coded for MOBILE-FRIENDLINESS & WordPress friendly Ideal.

5. This is the first, small job of many we/graphic design jobs. If suits, winning designer may be offered all future work direct.

Thanks & look forward to your design. Glen.

Target Market(s)

corporates - high end

Number of Pages Required

2 page

Font styles to use
Sans Serif

Requirements
Must have
• Classy professional look
Nice to have
• all in Video in brief
Should not have
• too many images / new images I haven't approved

```html
<!DOCTYPE html>
<html lang="en">
<head>
<meta charset="utf-8">
<title>Podium Voice Hub – Find the Perfect Speaker</title>
<link href="https://fonts.googleapis.com/css2?family=Open+Sans:wght@400;600;700&display=swap" rel="stylesheet">
<style>
:root{
  --blue:#1f5fa8;
  --navy:#173e6e;
  --orange:#e2581d;
  --text:#3d4650;
  --muted:#6b7580;
  --tile:#dcecf7;
  --tile-line:#bcd6ea;
  --note-bg:#eef1f4;
  --hero-dark:#2a2f36;
  --white:#ffffff;
}
*{box-sizing:border-box;margin:0;padding:0}
html,body{width:814px;height:1200px;overflow:hidden;background:var(--white)}
body{font-family:"Open Sans",Arial,sans-serif;color:var(--text);font-size:12px;line-height:1.45}
.page{position:relative;width:814px;height:1200px}

.site-header{height:56px;display:flex;align-items:center;justify-content:space-between;padding:0 22px 0 20px;border-bottom:1px solid #e3e7eb}
.site-header h1{font-size:19px;font-weight:700;color:var(--blue);line-height:1.15}
.site-header .tagline{font-size:13px;color:var(--orange);font-weight:600}
.contact-buttons{display:flex;gap:10px}
.btn-outline{display:inline-flex;align-items:center;gap:6px;border:1px solid var(--blue);color:var(--blue);font-size:12px;font-weight:600;padding:6px 12px;border-radius:2px;background:var(--white)}
.btn-outline svg{width:14px;height:14px}

.hero{position:relative;height:292px;background:linear-gradient(90deg,#1c2026 0%,#30363e 55%,#4a4f56 100%);overflow:hidden}
.hero-photo{position:absolute;right:0;top:0;width:380px;height:292px;background:radial-gradient(ellipse at 60% 45%,#8a8074 0%,#5b5650 45%,rgba(48,54,62,0) 80%)}
.hero-copy{position:absolute;left:30px;top:30px;color:var(--white);font-size:25px;font-weight:400;line-height:1.22;width:380px}
.hero-copy strong{font-weight:700}
.hero-copy p+p{margin-top:18px}
.btn-orange{display:inline-block;background:var(--orange);color:var(--white);font-weight:700;font-size:11px;padding:8px 16px;border-radius:2px;text-transform:uppercase}
.hero .btn-orange{position:absolute;left:30px;top:240px}

.intro{display:flex;gap:26px;padding:22px 28px 0 34px;height:290px;position:relative}
.intro-text{width:350px;font-size:11.5px}
.intro-text p{margin-bottom:10px}
.intro-text b{color:#222}
.arrow{position:absolute;left:280px;top:210px;width:120px;height:60px}
.video-col{flex:1;display:flex;flex-direction:column;align-items:center}
.video{width:100%;height:186px;background:linear-gradient(180deg,#d7dadd,#b9bec3);border:1px solid #c8ccd0;position:relative}
.video-bar{position:absolute;left:0;right:0;bottom:0;height:18px;background:#2c3035}
.video-bar span{position:absolute;left:8px;top:5px;width:0;height:0;border-left:8px solid #fff;border-top:4px solid transparent;border-bottom:4px solid transparent}
.video-col .btn-orange{margin-top:12px;font-size:11px}

.tiles{display:flex;gap:10px;padding:0 28px;margin-top:6px}
.tile{flex:1;background:var(--tile);border:1px solid var(--tile-line);height:126px;text-align:center;padding:10px 8px}
.tile svg{width:34px;height:34px}
.tile h3{font-size:12px;font-weight:700;color:var(--navy);margin-top:4px}
.tile p{font-size:10.5px;color:var(--text);line-height:1.35}

.closing{padding:14px 28px 0 28px;font-size:11.5px}
.action-row{display:flex;justify-content:space-between;align-items:center;padding:22px 28px 0 28px}
.action-row .btn-orange{font-size:12px;padding:11px 30px}
.action-row .contact-buttons .btn-outline{padding:9px 14px}

.notes{position:absolute;left:0;right:0;top:880px;height:262px;background:var(--note-bg);padding:16px 34px}
.notes h2{font-size:14px;color:var(--navy);font-weight:700;margin-bottom:10px}
.notes li{list-style:none;position:relative;padding-left:16px;margin-bottom:12px;font-size:11.5px}
.notes li::before{content:"";position:absolute;left:0;top:5px;border-left:6px solid var(--blue);border-top:4px solid transparent;border-bottom:4px solid transparent}

.site-footer{position:absolute;left:0;right:0;bottom:0;height:58px;background:var(--navy);color:#c9d6e6;font-size:9.5px;text-align:center;padding-top:16px;line-height:1.5}
</style>
</head>
<body>
<div class="page">
  <header class="site-header">
    <div>
      <h1>Find the Perfect Speaker for Your Next Event Here...</h1>
      <div class="tagline">Free Industry Service</div>
    </div>
    <div class="contact-buttons">
      <span class="btn-outline"><svg viewBox="0 0 16 16"><rect x="1" y="3" width="14" height="10" fill="none" stroke="currentColor" stroke-width="1.5"/><path d="M1 3l7 6 7-6" fill="none" stroke="currentColor" stroke-width="1.5"/></svg>EMAIL US</span>
      <span class="btn-outline"><svg viewBox="0 0 16 16"><path d="M4 1l3 3-2 2c1 2 3 4 5 5l2-2 3 3-2 3C7 14 2 9 1 4z" fill="currentColor"/></svg>1300 48 62 17</span>
    </div>
  </header>

  <section class="hero">
    <div class="hero-photo" role="img" aria-label="Photo of a presenter in a suit gesturing towards the audience"></div>
    <div class="hero-copy">
      <p>Looking for a top <strong>motivational</strong> a guest speaker.</p>
      <p>MC, A Industry expert to "<strong>WOW</strong>" your next event?</p>
    </div>
    <span class="btn-orange">Find Her Here</span>
  </section>

  <section class="intro">
    <div class="intro-text">
      <p><b>Podium Voice Hub</b> is a <b>free industry service</b> designed to help people looking for speakers save precious time and frustration in finding the most suitable/best speaker for their needs.</p>
      <p>Suggestions are given by Australian conference speaker Glen Harlow, who has presented around Australia for a number of years and is familiar with many of our top professional speakers, MC's as well as the leading speaker bureaus.</p>
      <p>If you would like a hand finding some good speaker options, simply send us the details of your event and the type of presenter you are ideally after, e.g.</p>
    </div>
    <svg class="arrow" viewBox="0 0 120 60"><path d="M4 8 C30 50, 80 52, 112 40" fill="none" stroke="#9aa4ae" stroke-width="2"/><path d="M104 32l10 8-12 4" fill="none" stroke="#9aa4ae" stroke-width="2"/></svg>
    <div class="video-col">
      <div class="video" role="img" aria-label="Intro video of the speaker presenting"><div class="video-bar"><span></span></div></div>
      <span class="btn-orange">I want to make our event a great success</span>
    </div>
  </section>

  <section class="tiles">
    <div class="tile">
      <svg viewBox="0 0 34 34"><circle cx="17" cy="8" r="5" fill="var(--blue)"/><path d="M8 30l3-14h12l3 14z" fill="var(--blue)"/></svg>
      <h3>TYPE/STYLE</h3>
      <p>Motivational, Entertaining, Keynote/Workshop, MC etc</p>
    </div>
    <div class="tile">
      <svg viewBox="0 0 34 34"><rect x="4" y="6" width="26" height="18" fill="none" stroke="var(--blue)" stroke-width="2.5"/><path d="M17 24v6M11 30h12" stroke="var(--blue)" stroke-width="2.5"/></svg>
      <h3>TOPIC/AREA</h3>
      <p>Team Building, Leadership, Inspiration, Health/Life Balance etc</p>
    </div>
    <div class="tile">
      <svg viewBox="0 0 34 34"><rect x="4" y="8" width="26" height="18" rx="2" fill="var(--blue)"/><circle cx="17" cy="17" r="5" fill="var(--tile)"/></svg>
      <h3>APPROXIMATE BUDGE</h3>
      <p>$1000, $2500, $5000, $7500+ etc</p>
    </div>
    <div class="tile">
      <svg viewBox="0 0 34 34"><path d="M17 3a9 9 0 0 0-9 9c0 7 9 19 9 19s9-12 9-19a9 9 0 0 0-9-9z" fill="var(--blue)"/><circle cx="17" cy="12" r="3.5" fill="var(--tile)"/></svg>
      <h3>LOCATION</h3>
      <p>Sydney, Melbourne, Brisbane, Perth, Adelaide, Canberra etc</p>
    </div>
  </section>

  <p class="closing">and where we can, we will be happy to send you some speaker possibilities/ideas, trusted speakers bureaus or simply some thoughts on the best places for you to look. Regards Glen S.</p>

  <div class="action-row">
    <span class="btn-orange">Quick Online Contact Form »</span>
    <div class="contact-buttons">
      <span class="btn-outline"><svg viewBox="0 0 16 16"><rect x="1" y="3" width="14" height="10" fill="none" stroke="currentColor" stroke-width="1.5"/><path d="M1 3l7 6 7-6" fill="none" stroke="currentColor" stroke-width="1.5"/></svg>EMAIL US</span>
      <span class="btn-outline"><svg viewBox="0 0 16 16"><path d="M4 1l3 3-2 2c1 2 3 4 5 5l2-2 3 3-2 3C7 14 2 9 1 4z" fill="currentColor"/></svg>1300 48 62 17</span>
    </div>
  </div>

  <section class="notes">
    <h2>Please Note:</h2>
    <ul>
      <li>Any information you provide will ONLY ever be used to help with your specific enquiry.</li>
      <li>Glen does not have any financial agreements with any individual speakers he recommends. He offers this service, as it only takes a few minutes of his time, helps promote other professional speakers and obviously keeps his own name out there in the industry.</li>
      <li>Please understand that while Glen tries to respond quickly, due to his own speaking/travel commitments it may take up to 24 hours.</li>
    </ul>
  </section>

  <footer class="site-footer">
    © 2015 All Rights Reserved www.podiumvoicehub.com.au PO Box 412 Sunshine NSW 2264<br>
    E-mail: hello@podiumvoicehub.com.au Phone: 1300 48 62 17
  </footer>
</div>
</body>
</html>
```